Criação de Papelaria Profissional para Construção & Engenharia
" Administração de obras: o cliente nos contrata para realizar a gestão da construção de sua casa (alto padrão), desde orçamentos, cronograma de obra, acompanhamento da obra e gestão da mão de obra. Desenvolvimento de novos negócios: Realizamos o estudo de viabilidade técnico-econômica de terrenos para realização de loteamentos, condomínios e empreendimentos verticais e prospectamos construtoras e loteadoras para apresentar o projeto. Gestão de Grupos de investimentos: Fracionamos investimentos do setor imobiliário em cotas para acelerar um determinado negócio. Ex: adquirimos um lote em condomínio, realizamos um projeto de casa alto padrão e calculamos o custo total entre terreno e obra. Fracionamos em contas de 50 mil e vendemos para arrecadar o valor total do investimento. Assim, construimos a casa e na hora da sua venda é dividido os lucros proporcionalmente as cotas adquiridas. "

```html
<!DOCTYPE html>
<html lang="pt-BR">
<head>
<meta charset="UTF-8">
<title>Cartão de Visitas — Torre Engenharia</title>
<link href="https://fonts.googleapis.com/css2?family=Montserrat:wght@400;500;700&display=swap" rel="stylesheet">
<style>
  :root {
    --navy: #1b3a63;
    --navy-deep: #12294a;
    --gold: #c9a869;
    --ink: #2a3445;
    --muted: #5d6675;
    --paper: #ffffff;
    --backdrop: #e4e5e7;
  }
  * { margin: 0; padding: 0; box-sizing: border-box; }
  html, body { width: 1200px; height: 1200px; overflow: hidden; }
  body {
    background: var(--backdrop);
    font-family: "Montserrat", sans-serif;
    display: flex;
    flex-direction: column;
    align-items: center;
    justify-content: center;
    gap: 60px;
  }
  .card {
    width: 840px;
    height: 480px;
    border-radius: 22px;
    position: relative;
    overflow: hidden;
    border-bottom: 8px solid var(--gold);
    box-shadow: 0 6px 18px rgba(0,0,0,.12);
  }
  .card-front {
    background: var(--paper);
    display: flex;
    align-items: center;
    padding: 0 60px;
  }
  .brand-block {
    width: 380px;
    display: flex;
    align-items: center;
    gap: 16px;
  }
  .brand-mark {
    width: 26px; height: 26px;
    border-radius: 50%;
    background: var(--gold);
    flex: none;
  }
  .brand-name {
    font-weight: 700;
    font-size: 36px;
    letter-spacing: 2px;
    color: var(--navy);
    line-height: 1.1;
  }
  .contact-block {
    flex: 1;
    display: flex;
    flex-direction: column;
    gap: 26px;
  }
  .contact-row {
    display: flex;
    align-items: center;
    gap: 18px;
    font-size: 20px;
    color: var(--ink);
  }
  .contact-row svg { width: 22px; height: 22px; flex: none; fill: var(--gold); }
  .person-name {
    font-weight: 700;
    font-size: 22px;
    color: var(--navy);
    text-transform: uppercase;
  }
  .person-role {
    font-size: 16px;
    color: var(--muted);
    margin-top: 4px;
  }
  .identity { margin-bottom: 14px; align-items: flex-start; }
  .card-back {
    background: linear-gradient(135deg, var(--navy) 0%, var(--navy-deep) 100%);
    display: flex;
    align-items: center;
    justify-content: center;
    gap: 22px;
  }
  .card-back .brand-name { color: #ffffff; font-size: 54px; letter-spacing: 4px; }
  .card-back .brand-mark { width: 34px; height: 34px; }
</style>
</head>
<body>
  <section class="card card-front" aria-label="Frente do cartão">
    <div class="brand-block">
      <span class="brand-mark"></span>
      <span class="brand-name">TORRE ENGENHARIA</span>
    </div>
    <div class="contact-block">
      <div class="contact-row identity">
        <svg viewBox="0 0 24 24"><circle cx="12" cy="7" r="5"/><path d="M2 23c0-6 4.5-9 10-9s10 3 10 9z"/></svg>
        <div>
          <div class="person-name">Marcos Andrade</div>
          <div class="person-role">Engenheiro Civil - CREA</div>
        </div>
      </div>
      <div class="contact-row">
        <svg viewBox="0 0 24 24"><path d="M6.6 10.8a15 15 0 0 0 6.6 6.6l2.2-2.2c.3-.3.7-.4 1-.2 1.1.4 2.3.6 3.6.6.6 0 1 .4 1 1V20c0 .6-.4 1-1 1C10.6 21 3 13.4 3 4c0-.6.4-1 1-1h3.5c.6 0 1 .4 1 1 0 1.3.2 2.5.6 3.6.1.3 0 .7-.2 1z"/></svg>
        <span>(47) 90000-1234</span>
      </div>
      <div class="contact-row">
        <svg viewBox="0 0 24 24"><path d="M2 5h20v14H2z M4 7v.5l8 5 8-5V7z" fill-rule="evenodd"/></svg>
        <span>contato@torreengenharia.com</span>
      </div>
      <div class="contact-row">
        <svg viewBox="0 0 24 24"><path d="M9 2a2 2 0 0 1 2 2v7l7 1.5c1 .2 1.7 1.2 1.5 2.2L18 22H8l-4-7 1.5-1.2L7 15V4a2 2 0 0 1 2-2z"/></svg>
        <span>www.torreengenharia.com</span>
      </div>
    </div>
  </section>

  <section class="card card-back" aria-label="Verso do cartão">
    <span class="brand-mark"></span>
    <span class="brand-name">TORRE ENGENHARIA</span>
  </section>
</body>
</html>
```